BKA

Please send us some options for letterhead I attached our Logo. In addition to the Logo we need this information somewhere on the page

47 Fenbury Lane
Easton Falls, CT 06412
203-481-7629

```html
<!DOCTYPE html>
<html lang="en">
<head>
<meta charset="utf-8">
<title>BKA Stationery</title>
<link rel="stylesheet" href="https://fonts.googleapis.com/css2?family=Open+Sans:wght@400;600;700;800&display=swap">
<style>
  :root {
    --blue: #1f80c6;
    --blue-deep: #135c9c;
    --blue-light: #cfe3f3;
    --brown: #4b3d38;
    --grey: #d3d4d6;
    --ink: #3a3a3a;
    --muted: #7b7b7b;
    --paper: #ffffff;
    --backdrop: #eeeeef;
  }
  * { box-sizing: border-box; margin: 0; padding: 0; }
  html, body { width: 1200px; height: 2400px; overflow: hidden; }
  body {
    background: var(--backdrop);
    font-family: "Open Sans", Arial, sans-serif;
    color: var(--ink);
    position: relative;
  }
  .sheet { position: absolute; background: var(--paper); box-shadow: 0 2px 10px rgba(0,0,0,.08); overflow: hidden; }

  /* brand lockup */
  .brand { display: flex; align-items: center; gap: 10px; }
  .brand-square { width: 30px; height: 30px; background: var(--brown); flex: none; }
  .brand-name { font-weight: 800; font-size: 30px; letter-spacing: 2px; color: var(--brown); line-height: 1; }

  /* letterhead */
  .letterhead { left: 220px; top: 60px; width: 760px; height: 1075px; }
  .letterhead .brand { position: absolute; left: 64px; top: 60px; }
  .letter { position: absolute; left: 64px; top: 170px; width: 560px; font-size: 12.5px; line-height: 1.6; }
  .letter p { margin-bottom: 16px; }
  .letter .recipient { margin-bottom: 22px; }
  .signature { width: 120px; height: 34px; margin: 6px 0 2px; background: linear-gradient(90deg, rgba(75,61,56,.35), rgba(75,61,56,.08)); border-radius: 3px; }
  .letter-footer { position: absolute; left: 0; right: 0; bottom: 30px; }
  .footer-rule { height: 3px; background: var(--blue); }
  .footer-contact { display: flex; justify-content: flex-end; gap: 22px; padding: 10px 64px 0; font-size: 12px; color: var(--muted); white-space: nowrap; }
  .contact-item { display: flex; align-items: center; gap: 6px; }
  .contact-item svg { width: 13px; height: 13px; fill: var(--blue); flex: none; }
  .base-band { position: absolute; left: 0; right: 0; bottom: 0; height: 18px; background: var(--brown); }

  /* business cards */
  .card { top: 1200px; width: 520px; height: 298px; }
  .card-front { left: 60px; }
  .card-front .brand { position: absolute; left: 36px; top: 36px; }
  .card-details { position: absolute; left: 36px; top: 110px; font-size: 13px; line-height: 1.55; }
  .card-name { font-weight: 700; font-size: 17px; color: var(--ink); }
  .card-title { color: var(--muted); margin-bottom: 8px; }
  .card-company { color: var(--blue); font-weight: 600; }
  .card-details .contact-item { color: var(--muted); }
  .card-back { left: 620px; background: radial-gradient(circle at 50% 50%, #6fb4e6 0%, var(--blue) 45%, var(--blue-deep) 100%); display: flex; align-items: center; justify-content: center; }
  .card-back .brand-square { background: var(--paper); }
  .card-back .brand-name { color: var(--paper); font-size: 40px; }
  .card-corner { position: absolute; right: 0; bottom: 0; width: 140px; height: 22px; background: var(--blue-light); }

  /* envelopes */
  .envelope { left: 220px; width: 760px; height: 372px; }
  .envelope-front { top: 1560px; }
  .envelope-front .brand { position: absolute; left: 40px; top: 40px; }
  .envelope-window { position: absolute; left: 380px; top: 230px; width: 320px; height: 90px; border-radius: 12px; background: var(--grey); }
  .envelope-back { top: 1962px; }
  .envelope-flap { position: absolute; left: 0; right: 0; top: 0; height: 110px; background: var(--blue); display: flex; align-items: center; justify-content: center; }
  .envelope-flap .brand-square { width: 18px; height: 18px; background: var(--paper); }
  .envelope-flap .brand-name { color: var(--paper); font-size: 20px; }
</style>
</head>
<body>

  <section class="sheet letterhead">
    <div class="brand"><span class="brand-square"></span><span class="brand-name">BKA</span></div>
    <div class="letter">
      <p class="recipient">November 1, 2013<br><br>Mr. Alan Hartwell<br>214 Brookside Lane<br>Norwalk, CT 06850</p>
      <p>Dear Mr. Hartwell,</p>
      <p>Thank you for taking the time to meet with our team last week. We appreciated the chance to learn more about your plans for the new home and the goals you have for your family over the coming years.</p>
      <p>As promised, we have reviewed the options that best fit your situation. Our advisors will prepare a clear summary of rates, terms and next steps, so that you can compare each choice with confidence before making any decision.</p>
      <p>Please feel free to call our office with any questions. We look forward to working with you and helping you move forward.</p>
      <p>Sincerely,</p>
      <div class="signature" role="img" aria-label="Handwritten signature"></div>
      <p>President</p>
    </div>
    <div class="letter-footer">
      <div class="footer-rule"></div>
      <div class="footer-contact">
        <span class="contact-item"><svg viewBox="0 0 24 24"><path d="M12 2a7 7 0 0 0-7 7c0 5 7 13 7 13s7-8 7-13a7 7 0 0 0-7-7zm0 9.5A2.5 2.5 0 1 1 12 6.5a2.5 2.5 0 0 1 0 5z"/></svg>47 Fenbury Lane | Easton Falls, CT 06412</span>
        <span class="contact-item"><svg viewBox="0 0 24 24"><path d="M6.6 10.8a15 15 0 0 0 6.6 6.6l2.2-2.2a1 1 0 0 1 1-.25 11.4 11.4 0 0 0 3.6.57 1 1 0 0 1 1 1V20a1 1 0 0 1-1 1A17 17 0 0 1 3 4a1 1 0 0 1 1-1h3.5a1 1 0 0 1 1 1c0 1.25.2 2.45.57 3.6a1 1 0 0 1-.25 1z"/></svg>203-481-7629</span>
      </div>
    </div>
    <div class="base-band"></div>
  </section>

  <section class="sheet card card-front">
    <div class="brand"><span class="brand-square"></span><span class="brand-name">BKA</span></div>
    <div class="card-details">
      <div class="card-name">Dana Corwell</div>
      <div class="card-title">Chief Executive Officer</div>
      <div class="card-company">BKA Group LLC</div>
      <div>47 Fenbury Lane</div>
      <div>Easton Falls, CT 06412</div>
      <span class="contact-item"><svg viewBox="0 0 24 24"><path d="M6.6 10.8a15 15 0 0 0 6.6 6.6l2.2-2.2a1 1 0 0 1 1-.25 11.4 11.4 0 0 0 3.6.57 1 1 0 0 1 1 1V20a1 1 0 0 1-1 1A17 17 0 0 1 3 4a1 1 0 0 1 1-1h3.5a1 1 0 0 1 1 1c0 1.25.2 2.45.57 3.6a1 1 0 0 1-.25 1z"/></svg>203-481-7629</span>
    </div>
    <div class="card-corner"></div>
  </section>

  <section class="sheet card card-back">
    <div class="brand"><span class="brand-square"></span><span class="brand-name">BKA</span></div>
  </section>

  <section class="sheet envelope envelope-front">
    <div class="brand"><span class="brand-square"></span><span class="brand-name">BKA</span></div>
    <div class="envelope-window"></div>
  </section>

  <section class="sheet envelope envelope-back">
    <div class="envelope-flap">
      <div class="brand"><span class="brand-square"></span><span class="brand-name">BKA</span></div>
    </div>
  </section>

</body>
</html>
```